Sponsored Fundraiser Needs Flyer

We need a flyer for a law firm sponsored fundraiser and community event. Pellmark Law Group is looking to become a familiar company for our community, and is hosting an Easter Egg Hunt & Yard Sale Fundraiser to raise money for the Miss Brightfield Service Pageant. See attached generic template for basic information.

Target Market(s)

Local Community

Industry/Entity Type

Community

Font styles to use
Decorative

Requirements
Must have
• Sponsorship information, fundraiser information, location information, website for fundraiser payments, logo for fundraiser group, logo for law group
Nice to have
• Colorful and inviting feel, eye catching designs

```html
<!DOCTYPE html>
<html lang="en">
<head>
<meta charset="utf-8">
<title>Easter Eggstravaganza Flyer</title>
<link href="https://fonts.googleapis.com/css2?family=Yellowtail&family=Damion&family=Fredoka:wght@600&family=Arimo:wght@400;700&display=swap" rel="stylesheet">
<style>
  :root{
    --mint-top:#c8ecd6;
    --mint-bottom:#9edad5;
    --coral:#e8474b;
    --berry:#d4457f;
    --berry-deep:#c23478;
    --leaf:#7dbf3f;
    --ink:#4f4f4f;
    --white:#ffffff;
    --navy:#1b2a57;
  }
  *{margin:0;padding:0;box-sizing:border-box}
  html,body{width:850px;height:1200px;overflow:hidden;background:#fff}
  .flyer{position:relative;width:850px;height:1200px;overflow:hidden;
    background:linear-gradient(180deg,var(--mint-top) 0%,var(--mint-bottom) 100%);
    font-family:"Arimo",Arial,sans-serif;color:var(--ink)}
  .egg-banner,.bottom-band,.bunny,.title{position:absolute}
  .egg-banner{left:0;top:0;width:850px;height:300px}
  .bottom-band{left:0;top:0;width:850px;height:1200px}
  .title{left:0;top:0;width:850px;height:420px}
  .title text{font-family:"Yellowtail","Damion",cursive;fill:var(--coral);
    stroke:var(--white);stroke-width:6px;paint-order:stroke fill;stroke-linejoin:round}
  .food-badge{position:absolute;left:622px;top:86px;width:172px;height:172px;border-radius:50%;
    background:var(--berry);border:5px solid var(--white);color:var(--white);
    text-align:center;transform:rotate(14deg);padding-top:14px;
    font-family:"Arimo",Arial,sans-serif;font-weight:700;font-size:16px;line-height:17px}
  .food-badge .free{font-family:"Yellowtail","Damion",cursive;font-weight:400;font-size:44px;line-height:44px;display:block;margin-bottom:2px}
  .venue{position:absolute;top:426px;left:0;width:850px;text-align:center;
    font-family:"Fredoka",sans-serif;font-weight:600;color:var(--coral)}
  .venue-name{font-size:32px;line-height:40px}
  .venue-address{font-size:22px;line-height:26px}
  .divider{position:absolute;left:140px;top:507px;width:570px;height:2px;background:var(--berry)}
  .highlights{position:absolute;top:522px;left:0;width:850px;text-align:center;
    font-weight:700;font-size:21px;line-height:28.8px;color:var(--berry)}
  .highlights .green{color:var(--leaf)}
  .story{position:absolute;top:680px;left:118px;width:614px;text-align:center;font-size:17.2px;line-height:23px}
  .story b{font-weight:700}
  .thanks{position:absolute;top:832px;left:130px;width:580px;text-align:center;
    font-weight:700;font-size:17px;line-height:20px;color:var(--berry-deep)}
  .pageant-mark{position:absolute;left:100px;top:930px;width:220px;text-align:center;
    color:var(--white);font-weight:700;font-size:17px;line-height:20px}
  .pageant-mark .dot{display:block;width:70px;height:70px;border-radius:50%;background:var(--white);margin:0 auto 10px}
  .register{position:absolute;left:20px;top:1064px;width:380px;text-align:center;color:var(--white);
    font-size:14.5px;line-height:16px}
  .register .url{font-weight:700}
  .register .small{font-size:12px;line-height:13px}
  .register .urgent{font-weight:700;font-size:12px;margin-top:6px}
  .sponsor{position:absolute;left:430px;top:1022px;width:410px;text-align:center;color:var(--white)}
  .sponsor-mark{display:flex;align-items:center;justify-content:center;gap:12px;margin-bottom:16px;margin-left:40px}
  .sponsor-mark .square{width:46px;height:46px;background:var(--navy);flex:none}
  .sponsor-mark .name{font-size:28px;line-height:30px;letter-spacing:1px;text-align:left;font-weight:400;color:var(--white)}
  .sponsor-contact{font-size:19px;line-height:21px}
</style>
</head>
<body>
<main class="flyer">
  <svg class="egg-banner" viewBox="0 0 850 300" role="img" aria-label="Row of colourful striped and patterned Easter eggs across the top">
    <defs>
      <linearGradient id="eggTones" x1="0" y1="0" x2="1" y2="0">
        <stop offset="0" stop-color="#f47a3a"/>
        <stop offset="0.3" stop-color="#f6b23a"/>
        <stop offset="0.55" stop-color="#9b88dc"/>
        <stop offset="0.75" stop-color="#4fb57a"/>
        <stop offset="1" stop-color="#ee4f77"/>
      </linearGradient>
    </defs>
    <path d="M0,0 H850 V230 C800,250 770,200 720,200 C650,200 620,230 560,190 C500,150 450,200 400,190 C330,180 300,250 230,240 C160,230 120,280 60,270 C30,265 10,275 0,280 Z" fill="url(#eggTones)"/>
  </svg>

  <svg class="bottom-band" viewBox="0 0 850 1200" aria-hidden="true">
    <path d="M0,700 C200,1020 600,1020 850,790 L850,1200 L0,1200 Z" fill="#d4457f"/>
  </svg>

  <div class="food-badge"><span class="free">Free</span>HOT DOGS,<br>HAMBURGERS,<br>CHIPS &amp;<br>DRINKS!</div>

  <svg class="title" viewBox="0 0 850 420">
    <title>Easter Eggstravaganza</title>
    <text x="232" y="282" font-size="150" textLength="330" lengthAdjust="spacingAndGlyphs">Easter</text>
    <text x="108" y="345" font-size="118" textLength="596" lengthAdjust="spacingAndGlyphs">Eggstravaganza</text>
  </svg>

  <div class="venue">
    <div class="venue-name">At Alder Creek Depot</div>
    <div class="venue-address">412 N Birch Loop Alder Creek AK 99610</div>
  </div>
  <div class="divider"></div>

  <div class="highlights">
    <div>FREE COMMUNITY EASTER EGG HUNT AT</div>
    <div class="green">THE ALDER CREEK DEPOT</div>
    <div>YARD SALE FUNDRAISER VENDORS WELCOME,</div>
    <div>“START YOUR SPRING CLEANING AND RESERVE A SPACE”</div>
    <div><span class="green">FACEPAINTING BY BRIGHT BRUSH FACES!</span> PRIZES!</div>
  </div>

  <p class="story">Our <b>Host Marianne</b> is a semi-finalist in the <b>Miss Brightfield Service Pageant</b> and is fundraising to provide our homeless female veterans with finance training, transitional housing, and job acquisiton support. For this event we are renting out booth spaces to sell your wares. It takes $25 a day to provide housing to a veteran, so we are renting booth space for $25 for the day. Set up can begin as early as 0800.</p>

  <p class="thanks">Special thanks to Pellmark Law Group for sponsoring the event. Visit www.pellmarklaw.com for all of your personal injury, slip and fall, or workers compensation questions.</p>

  <svg class="bunny" style="left:704px;top:808px;width:128px;height:192px" viewBox="0 0 128 192" role="img" aria-label="Cartoon white bunny holding a pink Easter egg">
    <rect x="0" y="0" width="128" height="192" rx="58" fill="#fbf4f2"/>
  </svg>

  <div class="pageant-mark"><span class="dot"></span>Miss Brightfield Service Pageant</div>

  <div class="register">
    <div>To register for a space please go to:</div>
    <div class="url">https://www.brightfieldgives.org/marianne2017/</div>
    <div>and click on the FundCircle link.</div>
    <div class="small">Post your $25 donation amount, with your name.<br>This will reserve your space. All proceeds go<br>directlay to <b>Homefront Haven Inc.</b></div>
    <div class="urgent">We only have 20 spaces so register now!</div>
  </div>

  <div class="sponsor">
    <div class="sponsor-mark"><span class="square"></span><span class="name">PELLMARK<br>LAW GROUP</span></div>
    <div class="sponsor-contact">Phone: (907) 555-0148<br>2280 Larkspur Lane<br>Suite 4 Northvale AK 99688<br>Email Address: nora@pellmarklaw.com</div>
  </div>
</main>
</body>
</html>
```